MSA Plans

I would like to rebuild my brochure for the 3 business plans that I currently offer my clients. I would like to make it look much more modern & attractive to clients when choosing one of our service plans. If we can stick to a tech theme that would be great. Message me for anymore information.

```html
<!DOCTYPE html>
<html lang="en">
<head>
<meta charset="utf-8">
<title>Brightdesk – Managed Services Framework</title>
<link href="https://fonts.googleapis.com/css2?family=Open+Sans:wght@400;600;700;800&display=swap" rel="stylesheet">
<style>
:root{
  --board:#4a4a4a;
  --orange:#f26522;
  --ink:#111111;
  --paper:#ffffff;
  --rule:#9a9a9a;
  --mist-light:#f3f3f3;
  --mist-dark:#d6d6d6;
}
*{box-sizing:border-box;margin:0;padding:0}
html,body{width:1200px;height:676px;overflow:hidden;background:var(--board);font-family:'Open Sans',sans-serif;color:var(--ink)}
.board{position:relative;width:1200px;height:676px}
.page-label{position:absolute;top:56px;width:353px;text-align:center;color:#fff;font-weight:800;font-size:28px;letter-spacing:.5px}
.page{position:absolute;top:111px;width:353px;height:499px;background:var(--paper);box-shadow:0 2px 6px rgba(0,0,0,.45);overflow:hidden}
.col-1{left:40px}.col-2{left:425px}.col-3{left:808px}

/* brand */
.brand{display:flex;align-items:center;justify-content:center;gap:6px}
.brand-mark{width:14px;height:14px;background:var(--orange);border-radius:50%}
.brand-name{font-weight:800;font-size:17px;letter-spacing:1.5px;color:var(--ink)}
.page-head{height:55px;border-bottom:1.5px solid var(--orange);display:flex;align-items:center;justify-content:center}

/* footer */
.page-foot{position:absolute;top:455px;left:0;right:0;height:44px;border-top:1.5px solid var(--orange);text-align:center;padding-top:5px;font-size:6.8px;line-height:8.3px;background:var(--paper)}
.page-foot .company{color:var(--orange);font-weight:700}

/* cover */
.cover-art{position:absolute;inset:0;background:radial-gradient(circle at 45% 40%,var(--mist-light),var(--mist-dark))}
.cover-brand{position:absolute;top:186px;left:0;right:0}
.cover-brand .brand-mark{width:22px;height:22px}
.cover-brand .brand-name{font-size:28px;letter-spacing:2px}
.cover-title{position:absolute;top:226px;left:0;right:0;text-align:center;color:var(--orange);font-weight:700;font-size:16px}
.cover-version{position:absolute;top:254px;left:74px;width:204px;height:18px;background:var(--orange);color:#fff;font-weight:700;font-size:11px;line-height:18px;text-align:center}
.cover-band{position:absolute;top:436px;left:0;right:0;height:19px;background:var(--orange);color:#fff;font-weight:700;font-size:7.6px;line-height:19px;text-align:center}
.col-1 .page-foot{border-top:none;top:455px}

/* plan tables */
.plan-table{position:absolute;top:68px;left:22px;width:308px;border-collapse:collapse;font-size:5.5px;table-layout:fixed}
.plan-table td,.plan-table th{border:0.6px solid var(--rule);height:11.3px;padding:0 4px;text-align:center;vertical-align:middle;white-space:nowrap}
.plan-table td:first-child{text-align:left}
.plan-table .head th{background:var(--ink);color:#fff;font-weight:700;font-size:6.6px;height:14px;border-color:var(--ink)}
.plan-table .head th:first-child{text-align:left}
.plan-table .section td{background:var(--orange);color:#fff;font-weight:700;font-size:6.5px;height:10.5px;border-color:var(--orange)}
.plan-table .gap td{height:4px;border:none;padding:0}
.plan-table .price td{background:var(--ink);color:#fff;font-weight:700;font-size:6px;border-color:#555}
.plan-table .price td:first-child{color:var(--orange)}
.icon{width:7.5px;height:7.5px;display:block;margin:0 auto}
.small{font-size:5px}
</style>
</head>
<body>
<svg width="0" height="0" style="position:absolute" aria-hidden="true">
  <symbol id="tick" viewBox="0 0 10 10"><circle cx="5" cy="5" r="4.3" fill="none" stroke="#f26522" stroke-width=".8"/><path d="M3 5.2l1.5 1.5L7.2 3.6" fill="none" stroke="#f26522" stroke-width=".9" stroke-linecap="round" stroke-linejoin="round"/></symbol>
  <symbol id="cross" viewBox="0 0 10 10"><circle cx="5" cy="5" r="4.3" fill="none" stroke="#111" stroke-width=".8"/><path d="M3.4 3.4l3.2 3.2M6.6 3.4L3.4 6.6" stroke="#111" stroke-width=".9" stroke-linecap="round"/></symbol>
</svg>

<main class="board">
  <h2 class="page-label" style="left:40px">MAIN PAGE</h2>
  <h2 class="page-label" style="left:425px">PAGE 1</h2>
  <h2 class="page-label" style="left:808px">PAGE 2</h2>

  <!-- Cover -->
  <section class="page col-1">
    <div class="cover-art" role="img" aria-label="Faded greyscale tech photo with gears and an orange connected-node network pattern"></div>
    <div class="brand cover-brand"><span class="brand-mark"></span><span class="brand-name">BRIGHTDESK</span></div>
    <h1 class="cover-title">Managed Services Framework</h1>
    <div class="cover-version">Version 1.0 | Updated: April 2024</div>
    <div class="cover-band">DEFINING OUR SERVICES AND HOW WE DELIVER THESE CONSISTENTLY TO YOU.</div>
    <footer class="page-foot">
      <div class="company">BRIGHTDESK IT SERVICES PTY LTD | ABN: 51 824 390 117</div>
      <div>brightdeskit.com.au | service@brightdeskit.com.au | 1300 555 019</div>
      <div>12/48 Harlow St, Westmere, VIC, 3099</div>
    </footer>
  </section>

  <!-- Page 1 -->
  <section class="page col-2">
    <header class="page-head"><div class="brand"><span class="brand-mark"></span><span class="brand-name">BRIGHTDESK</span></div></header>
    <table class="plan-table">
      <colgroup><col style="width:153px"><col style="width:47px"><col style="width:52px"><col style="width:56px"></colgroup>
      <tr class="head"><th>Managed Services Agreement</th><th>Essential</th><th>Business</th><th>Professional</th></tr>
      <tr class="section"><td colspan="4">Support</td></tr>
      <tr><td>Unlimited Remote Support 7am to 6pm</td><td><svg class="icon"><use href="#tick"/></svg></td><td><svg class="icon"><use href="#tick"/></svg></td><td><svg class="icon"><use href="#tick"/></svg></td></tr>
      <tr><td>3<sup>rd</sup> Party Vendor Support</td><td><svg class="icon"><use href="#tick"/></svg></td><td><svg class="icon"><use href="#tick"/></svg></td><td><svg class="icon"><use href="#tick"/></svg></td></tr>
      <tr><td>Reactive Onsite Support 8am to 5pm</td><td>VIP Rates</td><td><svg class="icon"><use href="#tick"/></svg></td><td><svg class="icon"><use href="#tick"/></svg></td></tr>
      <tr><td>After-Hours Support</td><td>VIP Rates</td><td>VIP Rates</td><td><svg class="icon"><use href="#tick"/></svg></td></tr>
      <tr class="section"><td colspan="4">Service</td></tr>
      <tr><td>Guaranteed SLA Response Times</td><td><svg class="icon"><use href="#tick"/></svg></td><td><svg class="icon"><use href="#tick"/></svg></td><td><svg class="icon"><use href="#tick"/></svg></td></tr>
      <tr><td>24x7 Website &amp; Infrastructure Monitoring</td><td><svg class="icon"><use href="#tick"/></svg></td><td><svg class="icon"><use href="#tick"/></svg></td><td><svg class="icon"><use href="#tick"/></svg></td></tr>
      <tr><td>Secure Web Content Filtering</td><td><svg class="icon"><use href="#tick"/></svg></td><td><svg class="icon"><use href="#tick"/></svg></td><td><svg class="icon"><use href="#tick"/></svg></td></tr>
      <tr><td>Backup Monitoring</td><td><svg class="icon"><use href="#tick"/></svg></td><td><svg class="icon"><use href="#tick"/></svg></td><td><svg class="icon"><use href="#tick"/></svg></td></tr>
      <tr><td>Workstation OS Patching &amp; Updating</td><td><svg class="icon"><use href="#tick"/></svg></td><td><svg class="icon"><use href="#tick"/></svg></td><td><svg class="icon"><use href="#tick"/></svg></td></tr>
      <tr><td>CEO / MD Home Tech Support</td><td><svg class="icon"><use href="#tick"/></svg></td><td><svg class="icon"><use href="#tick"/></svg></td><td><svg class="icon"><use href="#tick"/></svg></td></tr>
      <tr><td>Monthly Tech Site Visit</td><td><svg class="icon"><use href="#cross"/></svg></td><td>Quarterly</td><td>Monthly</td></tr>
      <tr><td>Short Term Loan Equipment</td><td><svg class="icon"><use href="#cross"/></svg></td><td>1 Month</td><td>3 Months</td></tr>
      <tr><td>Adds / Moves / Changes (Staff)</td><td><svg class="icon"><use href="#tick"/></svg></td><td><svg class="icon"><use href="#tick"/></svg></td><td><svg class="icon"><use href="#tick"/></svg></td></tr>
      <tr><td>Adds / Moves / Changes (Workstations)</td><td>VIP Rates</td><td>VIP Rates</td><td><svg class="icon"><use href="#tick"/></svg></td></tr>
      <tr class="section"><td colspan="4">Management</td></tr>
      <tr><td>Asset and Warranty Tracking &amp; Reporting</td><td><svg class="icon"><use href="#tick"/></svg></td><td><svg class="icon"><use href="#tick"/></svg></td><td><svg class="icon"><use href="#tick"/></svg></td></tr>
      <tr><td>Comprehensive IT Documentation</td><td><svg class="icon"><use href="#tick"/></svg></td><td><svg class="icon"><use href="#tick"/></svg></td><td><svg class="icon"><use href="#tick"/></svg></td></tr>
      <tr><td>Technology Strategy Meeting</td><td>Annual</td><td>Quarterly</td><td>Monthly</td></tr>
      <tr><td>Technology Business Review Meeting</td><td>Annual</td><td>Bi Annual</td><td>Quarterly</td></tr>
      <tr><td>IT Policy Templates</td><td><svg class="icon"><use href="#cross"/></svg></td><td><svg class="icon"><use href="#tick"/></svg></td><td><svg class="icon"><use href="#tick"/></svg></td></tr>
      <tr class="section"><td colspan="4">Training</td></tr>
      <tr><td>End User Training Materials</td><td><svg class="icon"><use href="#cross"/></svg></td><td><svg class="icon"><use href="#cross"/></svg></td><td><svg class="icon"><use href="#tick"/></svg></td></tr>
      <tr><td>Security Awareness Training</td><td><svg class="icon"><use href="#tick"/></svg></td><td><svg class="icon"><use href="#tick"/></svg></td><td><svg class="icon"><use href="#tick"/></svg></td></tr>
      <tr class="gap"><td colspan="4"></td></tr>
      <tr class="price"><td>RRP / User</td><td>$110</td><td>$130</td><td>$165</td></tr>
      <tr class="price"><td>Minimum User Count</td><td>5</td><td>5</td><td>5</td></tr>
      <tr class="price"><td>Minimum Monthly Commit</td><td>$550</td><td>$650</td><td>$825</td></tr>
    </table>
    <footer class="page-foot">
      <div class="company">BRIGHTDESK IT SERVICES PTY LTD | ABN: 51 824 390 117</div>
      <div>brightdeskit.com.au | service@brightdeskit.com.au | 1300 555 019</div>
      <div>12/48 Harlow St, Westmere, VIC, 3099</div>
    </footer>
  </section>

  <!-- Page 2 -->
  <section class="page col-3">
    <header class="page-head"><div class="brand"><span class="brand-mark"></span><span class="brand-name">BRIGHTDESK</span></div></header>
    <table class="plan-table">
      <colgroup><col style="width:200px"><col style="width:52px"><col style="width:56px"></colgroup>
      <tr class="head"><th>Cybersecurity Packages</th><th>Business</th><th>Professional</th></tr>
      <tr><td>Compliance with National Cyber Baseline Maturity</td><td class="small">Level 0</td><td class="small">Level 1</td></tr>
      <tr><td>Security Standard - Alignment to Brightdesk Cloud Suite Security Policy &amp; Reporting</td><td><svg class="icon"><use href="#tick"/></svg></td><td><svg class="icon"><use href="#tick"/></svg></td></tr>
      <tr><td>24x7 Security Operations Centre (SOC) - Monitoring Cloud Suite</td><td><svg class="icon"><use href="#tick"/></svg></td><td><svg class="icon"><use href="#tick"/></svg></td></tr>
      <tr><td>Dark Web Scanning</td><td><svg class="icon"><use href="#tick"/></svg></td><td><svg class="icon"><use href="#tick"/></svg></td></tr>
      <tr><td>Cloud Email Filtering</td><td><svg class="icon"><use href="#tick"/></svg></td><td><svg class="icon"><use href="#tick"/></svg></td></tr>
      <tr><td>Cloud Suite Backup</td><td><svg class="icon"><use href="#tick"/></svg></td><td><svg class="icon"><use href="#tick"/></svg></td></tr>
      <tr><td>Automated Email Signatures</td><td><svg class="icon"><use href="#tick"/></svg></td><td><svg class="icon"><use href="#tick"/></svg></td></tr>
      <tr><td>Endpoint Protection with EDR - Workstations &amp; Servers</td><td><svg class="icon"><use href="#tick"/></svg></td><td><svg class="icon"><use href="#tick"/></svg></td></tr>
      <tr><td>3rd Party Applications Updating</td><td><svg class="icon"><use href="#cross"/></svg></td><td><svg class="icon"><use href="#tick"/></svg></td></tr>
      <tr><td>24x7 Security Operations Centre (SOC) - Monitoring Endpoints and Servers</td><td><svg class="icon"><use href="#cross"/></svg></td><td><svg class="icon"><use href="#tick"/></svg></td></tr>
      <tr><td>Privileged Access Management &amp; Application Whitelisting</td><td><svg class="icon"><use href="#cross"/></svg></td><td><svg class="icon"><use href="#tick"/></svg></td></tr>
      <tr><td>Internal Vulnerability Scanning</td><td><svg class="icon"><use href="#cross"/></svg></td><td><svg class="icon"><use href="#tick"/></svg></td></tr>
      <tr><td>Backup &amp; Disaster Recovery to comply with National Cyber Baseline</td><td><svg class="icon"><use href="#cross"/></svg></td><td class="small">Pending Assessment</td></tr>
      <tr class="gap"><td colspan="3"></td></tr>
      <tr class="price"><td>RRP / User</td><td>$35</td><td>$60</td></tr>
      <tr class="price"><td>Minimum User Count</td><td>5</td><td>5</td></tr>
      <tr class="price"><td>Minimum Monthly Commit</td><td>$175</td><td>$300</td></tr>
    </table>
    <footer class="page-foot">
      <div class="company">BRIGHTDESK IT SERVICES PTY LTD | ABN: 51 824 390 117</div>
      <div>brightdeskit.com.au | service@brightdeskit.com.au | 1300 555 019</div>
      <div>12/48 Harlow St, Westmere, VIC, 3099</div>
    </footer>
  </section>
</main>
</body>
</html>
```